The Corvanta Group's website for high impact furniture promotions

I am looking for a simple website. we are a promotional company that runs events for furniture stores to increase sales for short periods of time. i would like the website to have about 4 areas to explain our company. I would like it to be simple and user friendly. I would like a link to chatterbook and a contact section. I am attaching our logo that i would like somewhere large or possibly in the backround. I am open to different color schemes. I would like to convey fast paced, modern, reliable. I am open to all different styles and look forward to seeing whats out there. we are looking for a quick turn around, so if we see one that we like quick, we will pick that one thanks
Updates
Project Deadline Extended
Reason: looking for some really creative designs and want to give a fair amount of time to produce
Target Market(s)
Retail Furniture store owners
Industry/Entity Type
It Company
Number of Pages Required
1 page
Colors
Designer to choose colors to be used in the design.
Look and feel
Each slider illustrates characteristics of the customer's brand and the style your logo design should communicate.

```html
<!DOCTYPE html>
<html lang="en">
<head>
<meta charset="utf-8">
<title>The Corvanta Group – High impact furniture promotions</title>
<link href="https://fonts.googleapis.com/css2?family=Playfair+Display:ital,wght@0,400;0,700;1,700&family=Open+Sans:wght@400;600;700&display=swap" rel="stylesheet">
<style>
  :root {
    --brown: #8a5a2b;
    --brown-dark: #7a4f26;
    --gold: #c9a06b;
    --accent: #e3a261;
    --navy: #232a44;
    --navy-deep: #1a1f35;
    --ink: #111111;
    --muted: #777777;
    --panel: #f5f5f5;
    --white: #ffffff;
  }
  * { margin: 0; padding: 0; box-sizing: border-box; }
  html, body { width: 1200px; height: 1000px; overflow: hidden; background: var(--white); }
  body { position: relative; font-family: "Open Sans", Arial, sans-serif; }

  .site-header { position: absolute; left: 0; top: 0; width: 1200px; height: 121px; border-bottom: 1px solid var(--gold); background: var(--white); }
  .brand { position: absolute; left: 235px; top: 38px; display: flex; align-items: center; gap: 10px; }
  .brand-mark { width: 40px; height: 40px; border-radius: 50%; background: var(--gold); }
  .brand-name { font-family: "Playfair Display", Georgia, serif; font-size: 17px; font-weight: 400; color: var(--brown); letter-spacing: 0.5px; }
  .main-nav { position: absolute; top: 52px; left: 621px; display: flex; gap: 31px; }
  .main-nav a { font-family: "Playfair Display", Georgia, serif; font-size: 14px; color: var(--brown); text-decoration: none; }
  .social-link { position: absolute; left: 945px; top: 51px; width: 21px; height: 21px; }

  .hero { position: absolute; left: 0; top: 121px; width: 1200px; height: 336px;
    background: linear-gradient(100deg, #2f3652 0%, #252c47 40%, #20263f 60%, #1b2036 100%); text-align: center; }
  .hero-title { position: absolute; left: 0; width: 100%; top: 100px; font-family: "Playfair Display", Georgia, serif; font-weight: 700; font-size: 37px; line-height: 38px; color: var(--white); }
  .hero-sub { position: absolute; left: 0; width: 100%; top: 200px; font-size: 8.5px; font-weight: 700; letter-spacing: 0.8px; color: var(--accent); }

  .intro { position: absolute; left: 0; top: 457px; width: 1200px; height: 459px; background: var(--panel); }
  .about { position: absolute; left: 235px; top: 78px; width: 345px; }
  .eyebrow { font-size: 8px; font-weight: 700; letter-spacing: 0.9px; color: var(--brown); }
  .about-title { margin-top: 8px; font-family: "Playfair Display", Georgia, serif; font-weight: 700; font-size: 17.5px; line-height: 22px; color: var(--ink); }
  .about-text { font-size: 9.3px; line-height: 17.3px; color: var(--muted); text-align: justify; }
  .about-text.first { margin-top: 26px; }
  .about-text + .about-text { margin-top: 6px; }
  .btn { position: absolute; left: 0; top: 275px; width: 119px; height: 28px; border-radius: 14px; background: var(--brown); color: var(--white); font-size: 9px; font-weight: 700; display: flex; align-items: center; justify-content: center; text-decoration: none; }

  .service-card { position: absolute; width: 168px; height: 146px; background: var(--white); border-bottom: 2px solid var(--brown); box-shadow: 0 2px 12px rgba(0,0,0,0.09); padding: 17px 21px 0 22px; }
  .service-title { font-family: "Playfair Display", Georgia, serif; font-weight: 700; font-size: 15px; color: var(--ink); }
  .service-title em { font-style: italic; }
  .service-text { margin-top: 4px; font-size: 9.2px; line-height: 14.5px; color: var(--muted); }
  .learn-more { position: absolute; left: 22px; top: 113px; font-size: 8px; font-weight: 600; color: var(--brown); text-decoration: none; display: flex; align-items: center; gap: 2px; }
</style>
</head>
<body>
  <header class="site-header">
    <div class="brand">
      <span class="brand-mark"></span>
      <span class="brand-name">The Corvanta Group</span>
    </div>
    <nav class="main-nav">
      <a href="#">Home</a>
      <a href="#">About Us</a>
      <a href="#">Services</a>
      <a href="#">Contact</a>
    </nav>
    <a class="social-link" href="#" aria-label="chatterbook">
      <svg width="21" height="21" viewBox="0 0 21 21"><circle cx="10.5" cy="10.5" r="9.8" fill="none" stroke="#c9a06b" stroke-width="1"/></svg>
    </a>
  </header>

  <section class="hero" role="img" aria-label="Dark blue interior photo of a patterned sofa with cushions beside a side table with a book and glass vases">
    <h1 class="hero-title">High impact<br>furniture promotions</h1>
    <p class="hero-sub">ETIAM CONSEQUAT QUAM AC SAGITTIS VIVERRA</p>
  </section>

  <section class="intro">
    <div class="about">
      <p class="eyebrow">ETIAM CONSEQUAT QUAM AC SAGITTIS VIVERRA</p>
      <h2 class="about-title">Lorem ipsum dolor sit amet, consectetur adipiscing elit. Pellentesque accumsan.</h2>
      <p class="about-text first">Vivamus eu neque ut sem malesuada consectetur sed sed felis. Vestibulum ante ipsum primis in faucibus orci luctus et ultrices posuere cubilia Curae. ullam et eros ornare, porttitor urna sed, auctor lacus. Morbi viverra lorem at neque tincidunt cons equat primis sem maledase ultrices.</p>
      <p class="about-text">Vivamus eu neque ut sem malesuada consectetur sed sed felis. Vestibulum ante ipsum primis in faucibus orci luctus et ultrices posuere cubilia Curae. ullam et eros ornare, porttitor urna sed, auctor lacus. Morbi viverra lorem at neque tincidunt cons equat primis sem maledase ultrices Vivamus eu neque ut sem malesuada consectetur sed sed felis.</p>
      <a class="btn" href="#">MORE ABOUT US</a>
    </div>

    <article class="service-card" style="left:610px; top:75px;">
      <h3 class="service-title">Services <em>1</em></h3>
      <p class="service-text">Vivamus eu neque ut seam mal suada consectetur sed sed felis Vestibulum ante ipsum primis in faucibus.</p>
      <a class="learn-more" href="#">Learn More <svg width="9" height="7" viewBox="0 0 9 7"><path d="M0 3.5h8M5 0.7l3 2.8-3 2.8" fill="none" stroke="#8a5a2b" stroke-width="1"/></svg></a>
    </article>
    <article class="service-card" style="left:797px; top:75px;">
      <h3 class="service-title">Services <em>2</em></h3>
      <p class="service-text">Vivamus eu neque ut seam mal suada consectetur sed sed felis Vestibulum ante ipsum primis in faucibus.</p>
      <a class="learn-more" href="#">Learn More <svg width="9" height="7" viewBox="0 0 9 7"><path d="M0 3.5h8M5 0.7l3 2.8-3 2.8" fill="none" stroke="#8a5a2b" stroke-width="1"/></svg></a>
    </article>
    <article class="service-card" style="left:610px; top:238px;">
      <h3 class="service-title">Services <em>3</em></h3>
      <p class="service-text">Vivamus eu neque ut seam mal suada consectetur sed sed felis Vestibulum ante ipsum primis in faucibus.</p>
      <a class="learn-more" href="#">Learn More <svg width="9" height="7" viewBox="0 0 9 7"><path d="M0 3.5h8M5 0.7l3 2.8-3 2.8" fill="none" stroke="#8a5a2b" stroke-width="1"/></svg></a>
    </article>
    <article class="service-card" style="left:797px; top:238px;">
      <h3 class="service-title">Services <em>4</em></h3>
      <p class="service-text">Vivamus eu neque ut seam mal suada consectetur sed sed felis Vestibulum ante ipsum primis in faucibus.</p>
      <a class="learn-more" href="#">Learn More <svg width="9" height="7" viewBox="0 0 9 7"><path d="M0 3.5h8M5 0.7l3 2.8-3 2.8" fill="none" stroke="#8a5a2b" stroke-width="1"/></svg></a>
    </article>
  </section>
</body>
</html>
```